Automotive component supplier needs a business card design

We need a business card design for our company called Velmar Global Components Ltd based in the UK. We are a supplier of interior and exterior components to premium car manufacturers such as Corvane Hale, Durrant Fyfe, Maxtorn and Valdessimo. We would like to see a modern business card design that uses the colour blue.

Target Market(s)

Premium automotive car manufacturers.

Industry/Entity Type

Automotive

Contact Information for Business Card

Company Name : Velmar Global Components Limited
Address: 17 Tamsey Yard, Upper Drisk, Warwick, CV31 8RJ, United Kingdom
Web Address : www.velmarparts-example.co.uk

Font styles to use
Other font styles liked:
• Helvetica

Colors
3176b5
0255a3
85acd3
cfdeed
cee9f5
85cae6
34a6d7
0692cd
9bcb3c

Requirements
Must have
• Clear company logo and a mixture of blue colours.
Nice to have
• A high quality modern image.
Should not have
• Multiple colours.

```html
<!DOCTYPE html>
<html lang="en">
<head>
<meta charset="utf-8">
<title>Velmar Global Components – Business Card</title>
<link rel="stylesheet" href="https://fonts.googleapis.com/css2?family=Ubuntu:wght@400;500;700&display=swap">
<style>
  :root {
    --bg: #eef0f2;
    --card-white: #fbfbfb;
    --blue-light: #a3c4e2;
    --blue-mid: #6e9fcf;
    --blue-deep: #3a78b8;
    --brand-blue: #3a90c8;
    --line-blue: #5a93cc;
    --ink: #3a3d42;
    --white: #ffffff;
  }
  * { box-sizing: border-box; margin: 0; padding: 0; }
  html, body {
    width: 1200px; height: 720px; overflow: hidden;
    background: var(--bg);
    font-family: "Ubuntu", sans-serif;
  }
  .canvas { position: relative; width: 1200px; height: 720px; }

  .card {
    position: absolute;
    width: 520px; height: 300px;
    border-radius: 4px;
    box-shadow: 0 10px 24px rgba(40, 60, 90, 0.18);
    overflow: hidden;
  }

  /* Front */
  .card-front {
    left: 50px; top: 70px;
    background: linear-gradient(200deg, var(--blue-light) 0%, var(--blue-mid) 55%, var(--blue-deep) 100%);
  }
  .front-wordmark {
    position: absolute; left: 46px; top: 88px;
    color: var(--white); font-weight: 700; line-height: 1;
  }
  .front-wordmark .name-main { display: block; font-size: 78px; letter-spacing: 2px; }
  .front-wordmark .name-sub { display: block; font-size: 21px; letter-spacing: 4.4px; margin-top: 12px; }

  /* Back */
  .card-back {
    left: 630px; top: 360px;
    background: var(--card-white);
  }
  .back-wordmark {
    position: absolute; left: 28px; top: 168px;
    color: var(--brand-blue); font-weight: 700; line-height: 1;
  }
  .back-wordmark .name-main { display: block; font-size: 38px; letter-spacing: 1px; }
  .back-wordmark .name-sub { display: block; font-size: 10.5px; letter-spacing: 2.1px; margin-top: 6px; }

  .contact-frame { position: absolute; inset: 0; }

  .contact-block {
    position: absolute; left: 318px; top: 66px;
    color: var(--ink); font-size: 11px; line-height: 1.4;
  }
  .address { margin-bottom: 12px; }
  .contact-list { list-style: none; }
  .contact-list li { display: flex; align-items: center; gap: 8px; margin-bottom: 8px; }
  .contact-list svg { width: 12px; height: 12px; flex: none; }
</style>
</head>
<body>
<main class="canvas">

  <section class="card card-front" aria-label="Business card front">
    <div class="front-wordmark">
      <span class="name-main">VELMAR</span>
      <span class="name-sub">GLOBAL COMPONENTS</span>
    </div>
  </section>

  <section class="card card-back" aria-label="Business card back">
    <div class="back-wordmark">
      <span class="name-main">VELMAR</span>
      <span class="name-sub">GLOBAL COMPONENTS</span>
    </div>

    <svg class="contact-frame" viewBox="0 0 520 300" aria-hidden="true">
      <path d="M520 34 L372 4 Q352 0 343 16 L290 112 Q285 122 286 134 L300 262 Q302 280 320 284 L420 300"
            fill="none" stroke="var(--line-blue)" stroke-width="1.4"/>
    </svg>

    <div class="contact-block">
      <p class="address">17 Tamsey Yard, Upper Drisk,<br>Warwick, CV31 8RJ<br>United Kingdom</p>
      <ul class="contact-list">
        <li>
          <svg viewBox="0 0 12 12"><rect x="3" y="0.8" width="6" height="10.4" rx="1.2" fill="none" stroke="var(--brand-blue)" stroke-width="1.1"/><circle cx="6" cy="9.4" r="0.6" fill="var(--brand-blue)"/></svg>
          <span>+44 1926 480 117</span>
        </li>
        <li>
          <svg viewBox="0 0 12 12"><path d="M2.2 1 L4.4 1 L5.2 3.6 L3.9 4.6 Q5 7.2 7.4 8.2 L8.4 6.9 L11 7.7 L11 9.8 Q10.6 11 9.4 11 Q4.5 10.5 1 3 Q1 1.4 2.2 1 Z" fill="var(--brand-blue)"/></svg>
          <span>+44 1926 480 118</span>
        </li>
        <li>
          <svg viewBox="0 0 12 12"><rect x="0.5" y="2" width="11" height="8" fill="var(--brand-blue)"/><path d="M0.8 2.4 L6 6.6 L11.2 2.4" fill="none" stroke="var(--white)" stroke-width="1"/></svg>
          <span>hello@velmarparts-example.co.uk</span>
        </li>
        <li>
          <svg viewBox="0 0 12 12"><circle cx="6" cy="6" r="5.5" fill="var(--brand-blue)"/><path d="M1 6 H11 M6 0.5 Q3 6 6 11.5 M6 0.5 Q9 6 6 11.5" fill="none" stroke="var(--white)" stroke-width="0.7"/></svg>
          <span>www.velmarparts-example.co.uk</span>
        </li>
      </ul>
    </div>
  </section>

</main>
</body>
</html>
```